Harborline Cremations Business Cards

To create a business card for my company Harborline Cremations. Remember it is a cremation company.
We want to make sure people have a business card and information. Something modern, professional
100% Online
Prices starting at $695 all-inclusive (prices subject to change without notice).
A business card is the first point of contact with the prospective client.

Contact Information for Business Card

(305) 418-7260
www.HarborlineCremationsMiami.example
harborlinecremations@mailbox.example

Requirements
Must have
• 100% Online
Prices starting at $695 all-inclusive (prices subject to change without notice)

(305) 418-7260

Must match logo style
Should not have
• No black backgrounds. Please only use the white, orange and blue from the logo

```html
<!DOCTYPE html>
<html lang="en">
<head>
<meta charset="utf-8">
<title>Harborline Cremations – Business Card</title>
<link rel="stylesheet" href="https://fonts.googleapis.com/css2?family=Arimo:ital,wght@0,400;0,700;1,700&display=swap">
<style>
  :root{
    --page:#ebe7e1;
    --orange:#e8692a;
    --orange-light:#f08a3e;
    --orange-deep:#d9501f;
    --blue:#1668b0;
    --blue-bright:#2a8fd8;
    --white:#ffffff;
    --card-light:#f4f4f3;
    --card-mid:#e3e5e6;
    --text-soft:#f7ede4;
  }
  html,body{margin:0;padding:0;width:1200px;height:970px;overflow:hidden;background:var(--page);}
  .card{
    position:absolute;left:100px;top:199px;width:1000px;height:572px;
    border-radius:22px;overflow:hidden;
    background:linear-gradient(135deg,var(--card-light),var(--card-mid));
    box-shadow:0 10px 30px rgba(0,0,0,.15);
    font-family:'Arimo',Arial,sans-serif;
  }
  .card-shapes{position:absolute;inset:0;}
  .holder{position:absolute;left:49px;top:76px;color:var(--text-soft);}
  .holder-name{margin:0;font-size:31px;font-weight:700;letter-spacing:.5px;}
  .holder-role{margin:2px 0 0;font-size:22px;font-weight:400;}
  .holder-rule{width:153px;height:3px;background:var(--text-soft);margin-top:10px;}
  .offer{position:absolute;left:49px;top:218px;font-style:italic;font-weight:700;}
  .offer-lead{margin:0;font-size:29px;color:var(--blue-bright);}
  .offer-line{margin:6px 0 0;font-size:24px;color:var(--text-soft);}
  .contacts{position:absolute;left:45px;top:382px;list-style:none;margin:0;padding:0;color:var(--text-soft);}
  .contacts li{display:flex;align-items:center;gap:9px;height:36px;font-size:20px;white-space:nowrap;}
  .contacts svg{width:28px;height:28px;flex:none;}
  .contacts .web{font-size:18.5px;}
  .brand{position:absolute;left:540px;width:460px;top:116px;text-align:center;}
  .brand-mark{width:220px;height:220px;border-radius:50%;background:var(--orange);margin:0 auto;}
  .brand-name{margin:22px 0 0;font-size:30px;font-weight:700;color:var(--blue);letter-spacing:2px;text-transform:uppercase;}
</style>
</head>
<body>
  <main class="card">
    <svg class="card-shapes" viewBox="0 0 1000 572" aria-hidden="true">
      <defs>
        <linearGradient id="panelFill" x1="0" y1="0" x2="1" y2="1">
          <stop offset="0" stop-color="var(--orange-light)"/>
          <stop offset=".6" stop-color="var(--orange)"/>
          <stop offset="1" stop-color="var(--orange-deep)"/>
        </linearGradient>
      </defs>
      <path d="M0 0 H540 C470 160 455 380 535 572 H0 Z" fill="url(#panelFill)"/>
      <path d="M548 0 C478 160 463 380 543 572" fill="none" stroke="var(--blue)" stroke-width="4"/>
    </svg>

    <section class="holder">
      <h1 class="holder-name">DANIEL REYES</h1>
      <p class="holder-role">Manager</p>
      <div class="holder-rule"></div>
    </section>

    <section class="offer">
      <p class="offer-lead">100% Online</p>
      <p class="offer-line">Starting at $695</p>
      <p class="offer-line">All-inclusive</p>
    </section>

    <ul class="contacts">
      <li>
        <svg viewBox="0 0 28 28" fill="none" stroke="currentColor" stroke-width="1.5"><circle cx="14" cy="14" r="12.5"/><rect x="10" y="7" width="8" height="14" rx="1.5"/><line x1="13" y1="18.5" x2="15" y2="18.5"/></svg>
        (305) 418-7260
      </li>
      <li>
        <svg viewBox="0 0 28 28" fill="none" stroke="currentColor" stroke-width="1.5"><circle cx="14" cy="14" r="12.5"/><rect x="8" y="9.5" width="12" height="9" rx="1"/><path d="M8 10 L14 15 L20 10"/></svg>
        harborlinecremations@mailbox.example
      </li>
      <li class="web">
        <svg viewBox="0 0 28 28" fill="none" stroke="currentColor" stroke-width="1.5"><circle cx="14" cy="14" r="12.5"/><circle cx="14" cy="14" r="7"/><ellipse cx="14" cy="14" rx="3" ry="7"/><line x1="7" y1="14" x2="21" y2="14"/></svg>
        www.HarborlineCremationsMiami.example
      </li>
    </ul>

    <section class="brand">
      <div class="brand-mark"></div>
      <p class="brand-name">Harborline Cremations</p>
    </section>
  </main>
</body>
</html>
```